Flyer for IT Support Company

We need a 1 sided A5 flyer to promote our services and support packages to local businesses, I have attached the sort of content and layout we are looking for but happy for you to be creative with backgrounds and colors. It needs to look modern and professional but catch the eye ;-)
The strap-line on the logo needs to be changed to to 'Your Local IT Company'

It Company

```html
<!DOCTYPE html>
<html lang="en">
<head>
<meta charset="utf-8">
<title>corvanet – IT Support Packages</title>
<link rel="stylesheet" href="https://fonts.googleapis.com/css2?family=Signika:wght@300;400;600;700&display=swap">
<style>
  :root {
    --green: #8cab2e;
    --green-dark: #6f8c1c;
    --green-light: #b5cc5a;
    --purple: #8a1b5e;
    --purple-dark: #6d1249;
    --ink: #1e1e1e;
    --rule: #3a3a3a;
    --paper: #ffffff;
  }
  * { box-sizing: border-box; margin: 0; padding: 0; }
  html, body { width: 846px; height: 1200px; overflow: hidden; background: var(--paper); }
  body { font-family: "Signika", sans-serif; color: var(--ink); position: relative; }

  .header-band {
    position: absolute; left: 0; top: 0; width: 846px; height: 118px;
    background: linear-gradient(90deg, var(--green-dark) 0%, var(--green) 45%, var(--green-light) 100%);
  }
  .header-art {
    position: absolute; left: 30px; top: 0; width: 260px; height: 110px;
    background: linear-gradient(160deg, rgba(255,255,255,0.18), rgba(255,255,255,0.02));
    border-radius: 0 0 30px 0;
  }
  .header-rule { position: absolute; left: 0; top: 118px; width: 846px; height: 8px; background: var(--purple); }

  .brand { position: absolute; right: 58px; top: 36px; text-align: right; color: #fff; }
  .brand-name { display: flex; align-items: center; gap: 8px; font-size: 50px; font-weight: 700; line-height: 1; letter-spacing: -1px; }
  .brand-dot { width: 36px; height: 36px; border-radius: 50%; background: #fff; }
  .brand-strap { font-size: 13px; font-weight: 600; letter-spacing: 1.6px; margin-top: 4px; }

  .headline { position: absolute; left: 58px; top: 142px; width: 570px; }
  .headline h1 { font-size: 30.5px; font-weight: 700; color: var(--green); line-height: 1.1; white-space: nowrap; }
  .headline h2 { font-size: 29.5px; font-weight: 700; color: var(--purple); line-height: 1.16; margin-top: 8px; }
  .headline p { font-size: 23.5px; font-weight: 700; color: var(--ink); margin-top: 6px; white-space: nowrap; }

  .price-badge {
    position: absolute; left: 622px; top: 110px; width: 166px; height: 166px; border-radius: 50%;
    background: radial-gradient(circle at 40% 35%, #a8327a, var(--purple) 60%, var(--purple-dark));
    border: 5px solid #fff; box-shadow: 0 3px 8px rgba(0,0,0,0.35);
    color: #fff; font-weight: 600; font-size: 16px; line-height: 1.15; text-align: center;
    display: flex; align-items: center; justify-content: center;
  }
  .price-badge span { display: block; transform: rotate(8deg); }

  .packages {
    position: absolute; left: 58px; top: 297px; width: 730px;
    border-collapse: collapse; font-size: 17px; table-layout: fixed;
  }
  .packages td, .packages th { border: 1px solid var(--rule); height: 25.76px; padding: 0 10px; }
  .packages col.label { width: 286px; }
  .packages col.tier { width: 111px; }
  .packages .tier-head th { background: var(--green); color: #fff; font-weight: 600; font-size: 18px; text-align: center; }
  .packages .section th { background: var(--purple); color: #fff; font-weight: 600; font-size: 18px; text-align: center; }
  .packages td { text-align: center; font-weight: 300; }
  .packages td:first-child { text-align: left; }
  .tick { color: var(--green); font-size: 17px; }

  .features { position: absolute; left: 58px; top: 958px; width: 730px; display: flex; justify-content: space-between; }
  .feature {
    width: 104px; height: 104px; border-radius: 50%; color: #fff; font-weight: 600; font-size: 14px; line-height: 1.25;
    display: flex; align-items: center; justify-content: center; text-align: center; padding: 0 4px;
    border: 3px solid #fff; box-shadow: 0 2px 6px rgba(0,0,0,0.35); white-space: nowrap;
  }
  .feature.purple { background: radial-gradient(circle at 40% 35%, #a8327a, var(--purple) 60%, var(--purple-dark)); }
  .feature.green { background: radial-gradient(circle at 40% 35%, #b4cc55, var(--green) 60%, var(--green-dark)); }

  .cta { position: absolute; left: 0; top: 1072px; width: 846px; text-align: center; font-size: 26px; font-weight: 700; }
  .contacts { position: absolute; left: 62px; top: 1122px; display: flex; align-items: center; font-size: 22px; font-weight: 700; color: var(--green); }
  .contacts svg { margin-right: 10px; }
  .contacts span { margin-right: 20px; }

  .footer-rule { position: absolute; left: 0; top: 1160px; width: 846px; height: 6px; background: var(--purple); }
  .footer-band { position: absolute; left: 0; top: 1166px; width: 846px; height: 34px; background: linear-gradient(90deg, var(--green-dark), var(--green), var(--green-light)); }
</style>
</head>
<body>
  <header>
    <div class="header-band"></div>
    <div class="header-art" role="img" aria-label="Faded laptop and light streaks across the green header"></div>
    <div class="header-rule"></div>
    <div class="brand">
      <div class="brand-name"><span class="brand-dot"></span>corvanet</div>
      <div class="brand-strap">YOUR LOCAL IT COMPANY</div>
    </div>
  </header>

  <section class="headline">
    <h1>AFFORDABLE IT SUPPORT PACKAGES</h1>
    <h2>PEACE OF MIND FOR YOUR BUSINESS AT COMPETITIVE PRICES</h2>
    <p>Protect your business and keep downtime costs at bay</p>
  </section>

  <div class="price-badge"><span>IT<br>Support<br>from £10pm<br>– from a trusted<br>provider based<br>in Ashbridge</span></div>

  <table class="packages">
    <colgroup><col class="label"><col class="tier"><col class="tier"><col class="tier"><col class="tier"></colgroup>
    <tr class="tier-head"><th>IT Support Packages</th><th>Remote</th><th>Plus</th><th>Pro</th><th>Unlimited</th></tr>
    <tr class="tier-head"><th>Per Server</th><th>£45pm</th><th>£85pm</th><th>£85pm</th><th>£85pm</th></tr>
    <tr class="tier-head"><th>Per Computers</th><th>£10pm</th><th>£10pm</th><th>£13pm</th><th>£15pm</th></tr>

    <tr class="section"><th colspan="5">Support service</th></tr>
    <tr><td>Server support</td><td class="tick">✓</td><td class="tick">✓</td><td class="tick">✓</td><td class="tick">✓</td></tr>
    <tr><td>PC/device support</td><td class="tick">✓</td><td class="tick">✓</td><td class="tick">✓</td><td class="tick">✓</td></tr>

    <tr class="section"><th colspan="5">Server/Network callout</th></tr>
    <tr><td>Remote support</td><td class="tick">✓</td><td class="tick">✓</td><td class="tick">✓</td><td class="tick">✓</td></tr>
    <tr><td>Onsite callout (4hr response)</td><td>£40</td><td class="tick">✓</td><td class="tick">✓</td><td class="tick">✓</td></tr>
    <tr><td>Hourly rate onsite</td><td>£25ph</td><td>Included</td><td>Included</td><td>Included</td></tr>

    <tr class="section"><th colspan="5">Computer/equipment/device callout</th></tr>
    <tr><td>Remote support</td><td class="tick">✓</td><td class="tick">✓</td><td class="tick">✓</td><td class="tick">✓</td></tr>
    <tr><td>Onsite callout (8hr response)</td><td>£40</td><td>£40</td><td class="tick">✓</td><td class="tick">✓</td></tr>
    <tr><td>Hourly rate onsite</td><td>£25ph</td><td>£25ph</td><td>Included</td><td>Included</td></tr>

    <tr class="section"><th colspan="5">Protection/Security</th></tr>
    <tr><td>DXR anti-virus (per PC)</td><td>£2</td><td>£2</td><td>£2</td><td class="tick">✓</td></tr>
    <tr><td>DXR content filter (per PC)</td><td>£1.30</td><td>£1.30</td><td>£1.30</td><td class="tick">✓</td></tr>
    <tr><td>Remote back-up (per unit , 5GB )</td><td>£1.50</td><td>£1.50</td><td>£1.50</td><td class="tick">✓</td></tr>

    <tr class="section"><th colspan="5">Monitoring</th></tr>
    <tr><td>Daily back-up checks</td><td class="tick">✓</td><td class="tick">✓</td><td class="tick">✓</td><td class="tick">✓</td></tr>
    <tr><td>24/7 monitoring</td><td class="tick">✓</td><td class="tick">✓</td><td class="tick">✓</td><td class="tick">✓</td></tr>

    <tr class="section"><th colspan="5">Maintenance</th></tr>
    <tr><td>Patch management</td><td class="tick">✓</td><td class="tick">✓</td><td class="tick">✓</td><td class="tick">✓</td></tr>
    <tr><td>Software updates</td><td class="tick">✓</td><td class="tick">✓</td><td class="tick">✓</td><td class="tick">✓</td></tr>
    <tr><td>Security updates</td><td class="tick">✓</td><td class="tick">✓</td><td class="tick">✓</td><td class="tick">✓</td></tr>
  </table>

  <div class="features">
    <div class="feature purple">Affordable,<br>Local Service</div>
    <div class="feature green">4<br>Hour<br>Callout</div>
    <div class="feature purple">Remote<br>Support</div>
    <div class="feature green">24/7<br>Monitoring</div>
    <div class="feature purple">Server/<br>PC Builds<br>From £250</div>
  </div>

  <p class="cta">Call, email or live chat with us on our website today!</p>

  <div class="contacts">
    <svg width="26" height="30" viewBox="0 0 26 30" aria-hidden="true"><path d="M6 2 L11 8 L8 12 C10 17 12 20 16 23 L20 20 L25 25 L21 29 C12 27 3 17 2 6 Z" fill="var(--purple)"/></svg>
    <span>01632 960 418</span>
    <svg width="44" height="28" viewBox="0 0 44 28" aria-hidden="true"><rect x="1" y="1" width="42" height="26" fill="none" stroke="var(--purple)" stroke-width="2"/><path d="M1 1 L22 16 L43 1 M1 27 L17 12 M43 27 L27 12" fill="none" stroke="var(--purple)" stroke-width="2"/></svg>
    <span>info@corvanet.co.uk</span>
    <svg width="34" height="34" viewBox="0 0 34 34" aria-hidden="true"><g fill="none" stroke="var(--purple)" stroke-width="2"><circle cx="17" cy="17" r="15"/><ellipse cx="17" cy="17" rx="7" ry="15"/><path d="M2 17 H32 M4 10 H30 M4 24 H30 M17 2 V32"/></g></svg>
    <span>www.corvanet.co.uk</span>
  </div>

  <footer>
    <div class="footer-rule"></div>
    <div class="footer-band"></div>
  </footer>
</body>
</html>
```